Business Card Re-Design for a Lighting Designer

I would like my business card re-designed. It is currently high gloss and they scratch too easily. I don not think the current design lends itself well to a matte finish. I have included the current design for reference along with our company logo.
Check out our website for current branding.
http://www.brambleorchidstudio.example

Updates
Some of the top contenders are muslim and it is a holiday for them. I do not want to discriminate and would expect the same courtesy for holidays we celebrate.
Target Market(s)
Interior Designers, Architects
Contact Information for Business Card
Logo - Name, Title, Address, Telephone Number and Extension, Email
Font styles to use
Requirements
Must have
- All the information listed on the current business card. If you use Red, it needs to be the red from our logo.
Nice to have
- Vertical and Horizontal Designs will be entertained.
Should not have
- Requirements for a glossy finish...should not look too corporate since we are a design firm.

```html
<!DOCTYPE html>
<html lang="en">
<head>
<meta charset="utf-8">
<title>Bramble Orchid Studio – Business Card</title>
<link rel="stylesheet" href="https://fonts.googleapis.com/css2?family=Raleway:wght@300;400;700&display=swap">
<style>
  :root {
    --logo-red: #b3060c;
    --icon-red: #e3141b;
    --deep-red: #5e0306;
    --near-black: #140203;
    --ink: #111111;
    --paper: #f4f4f4;
    --backdrop: #d9d6d2;
    --white: #ffffff;
    --muted: #d8c4c4;
  }
  * { box-sizing: border-box; margin: 0; padding: 0; }
  html, body { width: 1200px; height: 891px; overflow: hidden; }
  body {
    background: var(--backdrop);
    font-family: "Raleway", Arial, sans-serif;
    position: relative;
  }
  .card {
    position: absolute;
    top: 113px;
    width: 380px;
    height: 665px;
    overflow: hidden;
    box-shadow: 0 6px 18px rgba(0,0,0,.25);
  }
  .card--front { left: 190px; background: var(--paper); }
  .card--back {
    left: 630px;
    background: linear-gradient(160deg, var(--logo-red) 0%, #8a0408 45%, var(--deep-red) 75%, var(--near-black) 100%);
  }

  /* front */
  .front-shapes { position: absolute; inset: 0; }
  .brand {
    position: absolute; left: 34px; top: 70px; width: 320px;
    display: flex; align-items: center; gap: 16px;
  }
  .brand__square { width: 42px; height: 42px; background: var(--logo-red); flex: none; }
  .brand__name {
    font-weight: 300; font-size: 30px; line-height: 1.05;
    color: var(--ink); letter-spacing: 1px; text-transform: uppercase;
  }
  .tagline {
    position: absolute; left: 110px; top: 250px;
    font-size: 10px; letter-spacing: 2px; color: #bfbfbf; text-transform: uppercase;
  }
  .person { position: absolute; left: 40px; top: 345px; color: var(--white); }
  .person__name { font-weight: 700; font-size: 26px; letter-spacing: .5px; text-transform: uppercase; }
  .person__title { font-size: 14px; letter-spacing: 2px; margin-top: 4px; text-transform: uppercase; color: var(--muted); }
  .person__rule { width: 260px; height: 1px; background: rgba(255,255,255,.5); margin-top: 12px; }
  .contact { position: absolute; left: 40px; top: 440px; display: flex; gap: 14px; color: var(--white); }
  .contact__icons { display: flex; flex-direction: column; gap: 6px; padding-top: 50px; }
  .icon { width: 30px; height: 30px; background: var(--icon-red); display: flex; align-items: center; justify-content: center; }
  .contact__lines { font-size: 14px; line-height: 1.55; font-weight: 400; }
  .website {
    position: absolute; left: 40px; bottom: 34px;
    color: var(--white); font-weight: 700; font-size: 15px;
  }

  /* back */
  .back-art {
    position: absolute; left: 0; top: 0; width: 250px; height: 430px;
    background: linear-gradient(150deg, #c20a10 0%, #8d0509 60%, rgba(30,2,3,.9) 100%);
    clip-path: polygon(0 0, 100% 0, 100% 55%, 40% 100%, 0 100%);
  }
  .back-text {
    position: absolute; left: 290px; top: 150px;
    transform-origin: left top; transform: rotate(90deg);
    width: 460px; color: var(--white);
  }
  .back-text__studio {
    font-size: 20px; font-weight: 300; letter-spacing: 10px; text-transform: uppercase; color: #e9dede;
  }
  .back-text__tag { font-size: 13px; letter-spacing: 2px; margin-top: 8px; text-transform: uppercase; color: #d0bcbc; }
  .back-text__web { font-weight: 700; font-size: 15px; margin-top: 10px; }
</style>
</head>
<body>
  <section class="card card--front" aria-label="Business card front">
    <svg class="front-shapes" width="380" height="665" viewBox="0 0 380 665">
      <defs>
        <linearGradient id="lowerRed" x1="0" y1="0" x2="1" y2="1">
          <stop offset="0" stop-color="#8a0408"/>
          <stop offset="0.6" stop-color="#4a0205"/>
          <stop offset="1" stop-color="#140203"/>
        </linearGradient>
      </defs>
      <path d="M0 230 H380 V300 C300 300 250 320 220 340 L0 340 Z" fill="#111"/>
      <path d="M230 300 C290 270 340 275 380 280 V300 C320 300 270 318 240 340 Z" fill="#b3060c"/>
      <path d="M0 335 H215 C255 310 310 300 380 300 V665 H0 Z" fill="url(#lowerRed)"/>
      <path d="M0 335 H215 C255 310 310 300 380 300" fill="none" stroke="#fff" stroke-width="3"/>
    </svg>

    <div class="brand">
      <span class="brand__square"></span>
      <span class="brand__name">Bramble<br>Orchid Studio</span>
    </div>
    <p class="tagline">Lighting for Architecture</p>

    <div class="person">
      <h1 class="person__name">Maren Holloway</h1>
      <p class="person__title">Principle</p>
      <div class="person__rule"></div>
    </div>

    <div class="contact">
      <div class="contact__icons">
        <span class="icon" aria-label="Phone">
          <svg width="16" height="16" viewBox="0 0 16 16"><path d="M4 1 L6.5 4 L5 6 C6 8 8 10 10 11 L12 9.5 L15 12 L13 15 C7 15 1 9 1 3 Z" fill="#fff"/></svg>
        </span>
        <span class="icon" aria-label="Address">
          <svg width="16" height="16" viewBox="0 0 16 16"><path d="M8 1 C5 1 3 3.2 3 6 C3 10 8 15 8 15 C8 15 13 10 13 6 C13 3.2 11 1 8 1 Z" fill="#fff"/><circle cx="8" cy="6" r="2" fill="#e3141b"/></svg>
        </span>
        <span class="icon" aria-label="Email">
          <svg width="16" height="16" viewBox="0 0 16 16"><rect x="1" y="3.5" width="14" height="9" fill="#fff"/><path d="M1 3.5 L8 9 L15 3.5" fill="none" stroke="#e3141b" stroke-width="1.2"/></svg>
        </span>
      </div>
      <div class="contact__lines">
        <p>555.014.2290x1</p>
        <p>212 Linden Crossing Parkway, Suite 130</p>
        <p>Marietta, Georgia 30060 USA</p>
        <p>maren@brambleorchidstudio.example</p>
      </div>
    </div>

    <p class="website">www.brambleorchidstudio.example</p>
  </section>

  <section class="card card--back" aria-label="Business card back">
    <div class="back-art" role="img" aria-label="Large brand symbol area"></div>
    <div class="back-text">
      <p class="back-text__studio">Bramble Orchid Studio</p>
      <p class="back-text__tag">Lighting for Architecture</p>
      <p class="back-text__web">www.brambleorchidstudio.example</p>
    </div>
  </section>
</body>
</html>
```